Boracay Wedding Invitation Design

Hello, We would like a wedding invitation design for our wedding in Boracay. We would like it somewhat in the form of a boarding pass with beachy fresh colours, possibly a nice Boracay beach in the background Double sided with an envelope design to match. Maybe something simple on the envelope like a nice picture in the bottom left corner of a shell on a beach or something similar.

I would also like on the opposite side of the invite to be an "information sheet" with a matching beach design

The text files for both sides are included and i have also included 2 designs that i thought looked nice and are similar to what we are after.
Updates

Hello, I have updated the brief to be more specific with text files and images to make it easier for you. Thank you :)

Industry/Entity Type

Wedding

Font styles to use
Decorative
Script

Colors
fbee3d
33a6d7
33b8a4
fbf289
85cae6
ffffff

Requirements
Must have
• I would like to have this quote somewhere on the invitation
• This day I will marry my best friend,
• the one I laugh with,
• live for,
• dream with,
• love
• Owen & Marisa
• Request the pleasure of your company to celebrate their wedding
• On Friday the 17th March 2017
• at
• Velunda Grand Suites
• Boracay, Philippines
• Ceremony begins at 3.00pm
• RSVP
• Owen 0431907254
• Marisa 0417283649
• by
• 17th Jan 2016
• Dress: Beach Formal
• For the "information sheet"
• There will be a 5% discount on rooms booked at the Velunda under the event Owen & Marisa Wedding. The resort has a total of 24 rooms it would be nice if the majority of guests could stay at the resort from the night before until the night after the wedding but if you choose to stay elsewhere on the island there are plenty of other places to stay for cheaper and everything is fairly close as its a small island.
• We have currently blocked room stay for a short period of time so our guests can book rooms. If you choose to do so please email reservations@velundastays.example. Once rooms become available to the public again, towards the end of Jan, it will be first come first served basis. The resort is very popular so im assuming once this happens the rooms will be booked out.
• If you would like to check out the resort itself the website is www.velundagrand-isle.example
• We know its a fair distance to travel but we would really love to see you all there to celebrate and maybe even enjoy a small holiday while your here its a beautiful part of the world.
• If anyone has any questions please feel free to contact Owen on 0431907254
Nice to have
• A nice picture of a Boracay beach in the background would be nice

```html
<!DOCTYPE html>
<html lang="en">
<head>
<meta charset="utf-8">
<title>Owen &amp; Marisa – Wedding Invitation</title>
<link rel="stylesheet" href="https://fonts.googleapis.com/css2?family=Great+Vibes&family=Questrial&family=EB+Garamond&display=swap">
<style>
  :root {
    --ink: #1f9cc4;
    --ink-deep: #1784ab;
    --sea: #33b8c8;
    --sea-deep: #1d9fc9;
    --sky: #85cae6;
    --sand: #ece8e2;
    --sand-light: #f5f3ef;
    --white: #ffffff;
    --page: #e9eef1;
  }
  * { box-sizing: border-box; margin: 0; padding: 0; }
  html, body { width: 1200px; height: 1200px; overflow: hidden; }
  body {
    background: var(--page);
    font-family: "Questrial", sans-serif;
    color: var(--ink);
    position: relative;
  }

  /* ---------- invitation front ---------- */
  .invitation {
    position: absolute;
    left: 60px; top: 60px;
    width: 1080px; height: 500px;
    overflow: hidden;
    box-shadow: 0 6px 18px rgba(0,0,0,.18);
  }
  .invitation__photo {
    position: absolute; inset: 0;
    background:
      radial-gradient(ellipse 260px 200px at 82% 72%, rgba(255,255,255,.95), rgba(255,255,255,0) 70%),
      linear-gradient(180deg,
        #4fb2e4 0%, #2fb7cf 14%, #1fb1c7 28%, #6fcfd9 38%,
        #e8f4f6 46%, #dcdcd6 58%, var(--sand) 80%, #e6e1d9 100%);
  }
  .invitation__band {
    position: absolute; left: 0; right: 0; top: 0; height: 44px;
    background: linear-gradient(180deg, rgba(40,120,210,.55), rgba(40,120,210,0));
  }
  .stub {
    position: absolute; top: 0; bottom: 0;
  }
  .stub--left {
    left: 0; width: 130px;
    background: linear-gradient(180deg, rgba(133,202,230,.55), rgba(255,255,255,.25));
    border-right: 2px solid rgba(60,110,140,.35);
  }
  .stub--right {
    right: 0; width: 272px;
    background: rgba(255,255,255,.18);
    border-left: 2px solid rgba(60,110,140,.3);
    text-align: center;
    font-family: "EB Garamond", serif;
    color: var(--ink-deep);
  }
  .stub__title {
    position: absolute; left: 50%; top: 50%;
    transform: translate(-50%, -50%) rotate(-90deg);
    white-space: nowrap;
    font-family: "Great Vibes", cursive;
    font-size: 58px;
    color: var(--ink-deep);
  }
  .rsvp__heading { font-size: 38px; margin-top: 46px; letter-spacing: 1px; }
  .rsvp__lines { font-size: 21px; line-height: 36px; margin-top: 24px; }
  .rsvp__dress { font-size: 21px; position: absolute; left: 0; right: 0; top: 390px; }

  .main {
    position: absolute; left: 130px; width: 678px; top: 0; bottom: 0;
    text-align: center;
  }
  .main__names {
    font-family: "Great Vibes", cursive;
    font-size: 66px;
    color: var(--white);
    margin-top: 40px;
    line-height: 1;
    text-shadow: 0 1px 3px rgba(0,60,100,.3);
  }
  .main__request {
    font-variant: small-caps;
    font-size: 21px;
    letter-spacing: 1.5px;
    line-height: 26px;
    margin-top: 24px;
    color: var(--ink-deep);
  }
  .main__quote {
    font-family: "Great Vibes", cursive;
    font-size: 18px;
    line-height: 22px;
    margin-top: 8px;
    color: var(--ink-deep);
  }
  .main__details {
    font-size: 19px;
    line-height: 29px;
    letter-spacing: .8px;
    margin-top: 16px;
    color: var(--ink-deep);
  }

  /* ---------- information sheet ---------- */
  .info {
    position: absolute;
    left: 60px; top: 600px;
    width: 1080px; height: 500px;
    overflow: hidden;
    background: var(--sand-light);
    box-shadow: 0 6px 18px rgba(0,0,0,.18);
  }
  .info__photo {
    position: absolute; inset: 0;
    background:
      radial-gradient(ellipse 220px 260px at 50% 62%, rgba(200,200,200,.45), rgba(200,200,200,0) 70%),
      linear-gradient(180deg, #efedea, #e3ded7);
  }
  .info__curves { position: absolute; inset: 0; }
  .info__body {
    position: absolute; left: 150px; right: 150px; top: 20px; bottom: 20px;
    text-align: center;
    color: var(--ink);
  }
  .info__title { font-size: 31px; letter-spacing: 1.5px; font-weight: 400; }
  .info__para {
    font-size: 13.6px;
    line-height: 17px;
    letter-spacing: .6px;
    margin-top: 26px;
  }
  .info__para--tight { margin-top: 18px; }
  .info__contact {
    position: absolute; left: 0; right: 0; bottom: 18px;
    font-size: 15.5px;
    letter-spacing: .6px;
    color: var(--ink-deep);
    font-weight: 700;
  }
</style>
</head>
<body>

<section class="invitation" aria-label="Wedding invitation">
  <div class="invitation__photo" role="img" aria-label="Beach photograph: turquoise sea and white sand with white frangipani flowers in the lower right"></div>
  <div class="invitation__band"></div>

  <div class="stub stub--left">
    <span class="stub__title">Wedding Invitation</span>
  </div>

  <div class="main">
    <h1 class="main__names">Owen &amp; Marisa</h1>
    <p class="main__request">Request the pleasure of your company to celebrate<br>their wedding</p>
    <p class="main__quote">This day I will marry my best friend,<br>the one I laugh with,<br>live for,<br>dream with,<br>love</p>
    <p class="main__details">On Friday the 17th March 2017<br>at<br>Velunda Grand Suites<br>Boracay, Philippines<br>Ceremony begins at 3.00pm</p>
  </div>

  <div class="stub stub--right">
    <h2 class="rsvp__heading">RSVP</h2>
    <p class="rsvp__lines">Owen 0431907254<br>Marisa 0417283649<br>by<br>17th Jan 2016</p>
    <p class="rsvp__dress">Dress: Beach Formal</p>
  </div>
</section>

<section class="info" aria-label="Information sheet">
  <div class="info__photo" role="img" aria-label="Soft white sand photograph with a faint seashell in the centre"></div>
  <svg class="info__curves" width="1080" height="500" viewBox="0 0 1080 500" aria-hidden="true">
    <path d="M0 0 H70 Q150 250 70 500 H0 Z" fill="rgba(230,224,216,.9)"/>
    <path d="M1080 0 H1010 Q930 250 1010 500 H1080 Z" fill="rgba(230,224,216,.9)"/>
    <rect x="0" y="0" width="1080" height="500" fill="rgba(255,255,255,.35)"/>
  </svg>
  <div class="info__body">
    <h2 class="info__title">Information Sheet</h2>
    <p class="info__para info__para--tight">There will be a 5% discount on rooms booked at the Velunda under the event Owen &amp; Marisa Wedding. The resort has a total of 24 rooms it would be nice if the majority of guests could stay at the resort from the night before until the night after the wedding but if you choose to stay elsewhere on the island there are plenty of other places to stay for cheaper and everything is fairly close as its a small island.</p>
    <p class="info__para">We have currently blocked room stay for a short period of time so our guests can book rooms. If you choose to do so please email reservations@velundastays.example. Once rooms become available to the public again, towards the end of Jan, it will be first come first served basis. The resort is very popular so im assuming once this happens the rooms will be booked out.</p>
    <p class="info__para">If you would like to check out the resort itself the website is www.velundagrand-isle.example</p>
    <p class="info__para info__para--tight">We know its a fair distance to travel but we would really love to see you all there to celebrate and maybe even enjoy a small holiday while your here its a beautiful part of the world.</p>
    <p class="info__contact">If anyone has any questions please feel free to contact Owen on 0431907254</p>
  </div>
</section>

</body>
</html>
```